Zentaphone/Zentaslate App Developer Showcase Website (Redesign)

We need an attractive, modern and professional looking re-design of an existing website: www.kelvatro.com.

We have a new logo and want the website to use this - although the colors used in the logo could be altered to suit the website color scheme.

This site should consist of
- a main page showing off a few sample of apps
- a separate page for each app (one page template suitable for all apps)
- a few subsidiary pages which can be based on a single similar template, such as an About page, and Help pages for some of the apps

Note - some of the apps are Zentaphone only, and others are Zentaslate only or for both. Hence the design should allow for showing off both.

There is no need for the design to allow for lots of app screenshots (there will be links to the wareshelf where more screenshot can be seen).

It is not necessary to optimise the design just for Zentaphone screen viewing, but the
website should at least be reasonably usable on an Zentaphone and Zentaslate, as many users may be accessing the site from those devices.

Here are a few sites of similar developers - just for ideas. The first one listed is the one I think is the most attractive design. The main difference needed is that the primary function of this site is to show off the quality of the apps to app buyers, rather than to promote ourselves as app developers, which is only a secondary aim.

http://www.brindlecode.com.au/mobilebuilds.html
http://www.tarnlix.com.au/
http://www.quellomark.com/

Note - app screenshots and Zentaphone and Zentaslate device graphics templates (including glassy shadowed versions) are attached in a zip file.
Updates

Thank-you for all your submissions - your efforts are much appreciated. :-)

Seeing all the proposed designs has allowed me to see where I perhaps haven't been very clear in my brief, and also has helped me work out what type of design elements I prefer. So following is a refinement of the requirement.

The site requires only a simple layout ie.
At most it needs
- A Home page showing off a few screenshots, or with a scrolling/dynamic element, and a single link to keVTR in the wareshelf
- An About Us page
- A Contact Us page (with email form for two types are enquires a) App Support Enquiry b) Business Enquiry
- A Page for each app, including 
  > some phone/screenshot graphics
  > a description of the app features
  > a link to buy the app in the wareshelf
  > a Vidspree video demo link (for some apps only)
  > a link to a Help/FAQ page (for some apps only)

Note - if your design can show all the app info within the main page (eg. in a scrolling frame of some kind), then separate pages for each app might not even be required.

Things that are not needed are
- Request a Quote
- Follow us via Chatterfold, Peeplet etc...

Regarding the graphical design elements, I have decided that I do prefer
- designs with lighter colored backgrounds, so not black or very dark designs
- designs that keep the orange/black colors in the kelvatro logo, and use colors which work well with these

I will now contact some of you individually with specific feedback where I can - but there are so many designs already that I may not be able to contact everyone. If not, please do review your design in light of the above comments to see how well it fits.

Thanks again, and I am very pleased with results so far!

Target Market(s)

1. Zentaphone/Zentaslate owners looking for useful apps - tech savvy, well-educated
2. Companies/people looking for experienced/expert ZOS development company

Industry/Entity Type

It Professional

Requirements
Must have
• Expandable to allow new page to be added for each future apps

Use the attached new company logo design (although colors may be altered to suit website color scheme)

Site must be maintainable/expandable by ourselves once initial site is in place.
Nice to have
• Website nicely viewable from Zentaphone browser

Would be nice to have some dynamic elements eg. scrolling showcase of different app screens on main page

```html
<!DOCTYPE html>
<html lang="en">
<head>
<meta charset="utf-8">
<title>kelvatro — Skyvane Weather (Zentaslate)</title>
<link rel="stylesheet" href="https://fonts.googleapis.com/css2?family=Arimo&family=PT+Sans:wght@400;700&display=swap">
<style>
  :root {
    --bg: #f3f0ea;
    --text: #1e1e1e;
    --accent: #f29a0e;
    --btn-top: #7a7a7a;
    --btn-bottom: #3c3c3c;
    --btn-text: #ffffff;
    --frame: #cfcfcf;
    --device: #111111;
  }
  * { margin: 0; padding: 0; box-sizing: border-box; }
  html, body { width: 1200px; height: 800px; overflow: hidden; background: var(--bg); }
  body { position: relative; color: var(--text); font-family: "PT Sans", "Myriad Pro", sans-serif; }

  .brand { position: absolute; left: 72px; top: 46px; font-size: 46px; color: var(--accent); letter-spacing: -1px; line-height: 1; }

  .main-nav a { position: absolute; top: 62px; font-size: 29px; color: var(--text); text-decoration: none; line-height: 1; }
  .nav-apps { left: 327px; }
  .nav-about { left: 595px; }
  .nav-contact { left: 862px; }

  .device-glow { position: absolute; left: 48px; top: 110px; width: 560px; height: 560px;
    background: radial-gradient(circle, rgba(255,255,255,0.95) 0%, rgba(255,255,255,0.5) 40%, rgba(255,255,255,0) 68%); }
  .tablet { position: absolute; left: 186px; top: 206px; width: 285px; height: 366px;
    border: 2px solid var(--frame); border-radius: 20px;
    background: linear-gradient(135deg, #2a2a2a 0%, var(--device) 45%, #050505 100%);
    box-shadow: 0 10px 30px rgba(0,0,0,0.25); }
  .tablet-screen { position: absolute; left: 29px; top: 31px; width: 224px; height: 300px;
    background: linear-gradient(160deg, #4b6a88 0%, #a07a4a 35%, #8a6a3e 55%, #2c4f7e 80%, #233f6b 100%); }
  .tablet-home { position: absolute; left: 133px; top: 340px; width: 16px; height: 16px; border-radius: 50%;
    border: 1px solid #555; background: #0c0c0c; }

  .device-switch { position: absolute; top: 617px; width: 120px; text-align: center; font-size: 17px; font-weight: 700; line-height: 1; }
  .switch-phone { left: 224px; color: var(--text); }
  .switch-slate { left: 334px; color: var(--accent); }

  .app-title { position: absolute; left: 549px; top: 218px; font-size: 23px; font-weight: 400; line-height: 1.2; }
  .app-copy { position: absolute; left: 549px; top: 262px; width: 272px; font-family: "Arimo", Arial, sans-serif; font-size: 12px; line-height: 20px; }
  .app-copy p + p { margin-top: 20px; }

  .shot { position: absolute; top: 417px; width: 94px; height: 123px; }
  .shot-1 { left: 549px; background: linear-gradient(180deg, #5a5a5a, #6b5a48 50%, #4a4a4a); }
  .shot-2 { left: 665px; background: linear-gradient(160deg, #5a6f80, #9a7a4a 40%, #2c4f7e 85%); }
  .shot-3 { left: 783px; background: linear-gradient(180deg, #3e4646, #364242 50%, #3e3a38); }

  .btn { position: absolute; top: 609px; height: 29px; border-radius: 9px;
    background: linear-gradient(180deg, var(--btn-top), var(--btn-bottom));
    color: var(--btn-text); font-size: 17px; text-decoration: none; text-align: center; line-height: 29px; }
  .btn-buy { left: 548px; width: 65px; }
  .btn-video { left: 627px; width: 74px; }
  .btn-help { left: 716px; width: 98px; }

  .copyright { position: absolute; left: 0; width: 1083px; top: 708px; text-align: center; font-size: 16px; }
</style>
</head>
<body>
  <header>
    <div class="brand">kelvatro</div>
    <nav class="main-nav">
      <a class="nav-apps" href="#">Apps</a>
      <a class="nav-about" href="#">About us</a>
      <a class="nav-contact" href="#">Contact us</a>
    </nav>
  </header>

  <main>
    <div class="device-glow"></div>
    <div class="tablet">
      <div class="tablet-screen" role="img" aria-label="App screen showing a satellite map of Australia with forecast temperatures"></div>
      <div class="tablet-home"></div>
    </div>

    <span class="device-switch switch-phone">Zentaphone</span>
    <span class="device-switch switch-slate">Zentaslate</span>

    <h1 class="app-title">Skyvane Weather (Zentaslate)</h1>
    <div class="app-copy">
      <p>Accurate and frequently updated Australian weather forecasts, observations and radar loops from offical sources.</p>
      <p>Now available form the Wareshelf in Tunevault or on your Zentaphone!</p>
    </div>

    <div class="shot shot-1" role="img" aria-label="Screenshot of local weather observations"></div>
    <div class="shot shot-2" role="img" aria-label="Screenshot of the national forecast map"></div>
    <div class="shot shot-3" role="img" aria-label="Screenshot of weather trend graphs"></div>

    <a class="btn btn-buy" href="#">Buy</a>
    <a class="btn btn-video" href="#">Video</a>
    <a class="btn btn-help" href="#">App help</a>
  </main>

  <footer>
    <p class="copyright">© 2011 Merrowind Pty Ltd</p>
  </footer>
</body>
</html>
```